Redo a PPT pres. - Real Estate in Brazil - Socially equitable investments in Social Housing

We need to redo the presentation attached. It is an institutional presentation to attract local and foreign investors to invest in Brazilian Social Housing Projects structured by our company "RTV".
A middle class of 100 million, a housing deficit of 9M, a strong political will & positive income generation trends constitute grounds for a significant demand in social housing.
This make a perfect scheme for investors to invest in Brazilian Social Housing.
"RTV", is a consulting "boutique" focused in Brazilian real estate, specialized in structuring, analyzing and originating Brazilian social housing projects.
RTV is part of the group RTP. RTP is structured to create value through each step of the residential real estate business - structuring, financing, sales, marketing and technology.
We would like to see designs that use mainly the color blue. The final design should communicate financial safety and professionalism. In order to reach our needs, the designer will need to have basic understanding of finance and investment in order to highlight the most important information.
The idea is to receive back the PPT with each page redesigned and an homogeneous identity.
To all designers,
Target Market(s)
Institutional Investors and wealthy individuals
Industry/Entity Type
Residential
Look and feel
Each slider illustrates characteristics of the customer's brand and the style your logo design should communicate.

```html
<!DOCTYPE html>
<html lang="en">
<head>
<meta charset="utf-8">
<title>RTV – Social Housing in Brazil – Presentation Overview</title>
<link rel="stylesheet" href="https://fonts.googleapis.com/css2?family=Open+Sans:wght@400;600;700&family=PT+Serif:wght@400;700&display=swap">
<style>
:root{
  --bg:#e9edf2;
  --blue:#1a6fb5;
  --blue-dark:#0d4f8f;
  --blue-mid:#2d8fd6;
  --blue-light:#7cc4f0;
  --blue-pale:#dcecf8;
  --ink:#2b2b2b;
  --grey:#6b6b6b;
  --white:#ffffff;
  --red:#d6453a;
  --green:#7bb342;
}
*{box-sizing:border-box;margin:0;padding:0}
html,body{width:1200px;height:648px;overflow:hidden}
body{background:var(--bg);font-family:"Open Sans",Arial,sans-serif;color:var(--ink);position:relative}
.slide{position:absolute;width:305px;height:229px;background:var(--white);overflow:hidden;box-shadow:0 2px 6px rgba(0,0,0,.25)}
.s1{left:98px;top:63px}.s2{left:444px;top:63px}.s3{left:786px;top:63px}
.s4{left:84px;top:352px}.s5{left:444px;top:352px}.s6{left:790px;top:352px}
.slide-title{position:absolute;left:14px;top:8px;font-family:"PT Serif",Georgia,serif;font-weight:700;font-size:13px;color:var(--blue);padding-bottom:2px;border-bottom:1.5px solid var(--blue)}
.slide-sub{position:absolute;left:14px;top:31px;font-size:8px;color:var(--grey)}
.page-badge{position:absolute;right:-22px;bottom:-22px;width:66px;height:66px;border-radius:50%;border:2px solid var(--blue-light);background:var(--white)}
.page-num{position:absolute;right:12px;bottom:22px;font-family:"PT Serif",Georgia,serif;font-size:12px;color:var(--blue)}
.page-brand{position:absolute;right:6px;bottom:6px;font-family:"Open Sans",sans-serif;font-weight:700;font-size:8px;color:var(--blue-dark)}
.cover{background:linear-gradient(135deg,var(--blue-mid) 0%,var(--blue) 55%,var(--blue-dark) 100%)}
.cover-disc{position:absolute;border-radius:50%;background:var(--white);border:6px solid var(--blue-light)}
.s1 .cover-disc{left:105px;top:40px;width:300px;height:300px}
.cover-heading{position:absolute;left:8px;top:9px;color:var(--white);font-family:"PT Serif",Georgia,serif;z-index:2}
.cover-heading .kicker{font-size:11px;letter-spacing:.3px}
.cover-heading .line{font-size:10.5px;line-height:1.25}
.art{position:absolute}
.art-house{left:95px;top:40px;width:120px;height:130px;border-radius:8px;background:radial-gradient(circle at 50% 65%,#2f8ad0 0 28%,#f0c9a8 29% 55%,rgba(240,201,168,0) 70%)}
.art-family{left:0;bottom:0;width:95px;height:95px;background:linear-gradient(160deg,rgba(220,236,248,0) 0%,#c9d8e6 40%,#e7d3c0 100%)}
.brand{font-family:"Open Sans",sans-serif;font-weight:700;color:var(--blue-dark);display:flex;align-items:flex-end;gap:4px}
.brand .mark{display:inline-block;background:var(--blue-dark)}
.s1 .brand{position:absolute;left:158px;top:186px;font-size:30px}
.s1 .brand .mark{width:10px;height:10px;margin-bottom:8px}
.ring{position:absolute;left:70px;top:58px;width:165px;height:150px;border:1.5px solid #9ab6cf;border-radius:50%}
.pill{position:absolute;width:80px;height:20px;border-radius:10px;background:linear-gradient(#4aa3e6,var(--blue-dark));color:var(--white);font-size:4.6px;font-weight:600;text-align:center;display:flex;align-items:center;justify-content:center;line-height:1.15;padding:0 4px;box-shadow:0 1px 2px rgba(0,0,0,.35)}
.agenda{position:absolute;left:16px;top:33px;list-style:none;font-size:6px;font-weight:600;color:var(--ink)}
.agenda li{margin-bottom:5.3px;padding-left:9px;position:relative}
.agenda li::before{content:"";position:absolute;left:0;top:1.5px;width:4px;height:4px;border-radius:50%;background:var(--blue)}
.section-title{position:absolute;left:20px;top:140px;font-family:"PT Serif",Georgia,serif;font-weight:700;font-size:12px;color:var(--blue);border-bottom:1.5px solid var(--blue);padding-bottom:2px}
.section-pill{position:absolute;left:16px;top:172px;width:148px;height:28px;border-radius:14px;background:linear-gradient(#3d9be2,var(--blue-dark));color:var(--white);font-family:"PT Serif",Georgia,serif;font-weight:700;font-size:13px;line-height:28px;padding-left:22px;box-shadow:0 2px 4px rgba(0,0,0,.35)}
.section-pill .num{position:absolute;right:3px;top:2px;width:24px;height:24px;border-radius:50%;background:var(--blue-pale);color:var(--blue-dark);text-align:center;line-height:24px}
.card{position:absolute;background:var(--white);border-radius:6px;box-shadow:0 1px 4px rgba(0,0,0,.3);padding:18px 6px 4px;font-size:3.9px;line-height:1.35;color:var(--ink)}
.card-head{position:absolute;left:-2px;right:-2px;top:-4px;height:15px;border-radius:7px;background:linear-gradient(#4aa3e6,var(--blue-dark));color:var(--white);font-family:"PT Serif",Georgia,serif;font-weight:700;font-size:7.5px;text-align:center;line-height:15px}
.card p{margin-bottom:3px}
.card b{color:var(--blue-dark)}
.s4 .card-a{left:18px;top:72px;width:130px;height:146px}
.s4 .card-b{left:158px;top:72px;width:130px;height:100px}
.s5 .card-a{left:150px;top:68px;width:115px;height:118px;font-size:4.4px}
.charts{position:absolute;left:14px;top:52px}
.s6 .cover-disc{left:70px;top:-20px;width:270px;height:270px}
.s6 .brand{position:absolute;left:140px;top:88px;font-size:30px}
.s6 .brand .mark{width:10px;height:10px;margin-bottom:8px}
.thanks{position:absolute;left:135px;top:140px;font-family:"PT Serif",Georgia,serif;color:var(--blue);font-size:24px}
.thanks-sub{position:absolute;left:183px;top:170px;font-family:"PT Serif",Georgia,serif;font-size:11px;color:#111}
.s6 .art-family{left:0;bottom:0;width:85px;height:110px}
</style>
</head>
<body>

<section class="slide s1 cover" aria-label="Cover slide">
  <div class="cover-disc"></div>
  <div class="cover-heading">
    <div class="kicker">SOCIAL HOUSING IN BRAZIL</div>
    <div class="line">High Yield Return For</div>
    <div class="line">A Quasi Sovereign Risk</div>
  </div>
  <div class="art art-house" role="img" aria-label="Illustration of two hands forming a roof over a blue house"></div>
  <div class="art art-family" role="img" aria-label="Photo of a smiling family"></div>
  <div class="brand"><span class="mark"></span>RTV</div>
</section>

<section class="slide s2" aria-label="How to invest">
  <h2 class="slide-title">How To Invest In Social Housing In Brazil?</h2>
  <p class="slide-sub">A socially conscious &amp; lucrative investment</p>
  <div class="ring"></div>
  <div class="pill" style="left:112px;top:48px">Building housing units for low to middle-class buyers</div>
  <div class="pill" style="left:52px;top:88px">Target IRR<br>25-50%</div>
  <div class="pill" style="left:172px;top:88px">Investing in individual Projects</div>
  <div class="pill" style="left:40px;top:122px">Time Horizon<br>3-4 Years</div>
  <div class="pill" style="left:184px;top:122px">Management<br>Specialised International &amp; local team</div>
  <div class="pill" style="left:52px;top:157px">Equity participation of<br>R$2-10 millions</div>
  <div class="pill" style="left:172px;top:157px">Co-investing with local / mid-size developers</div>
  <div class="pill" style="left:112px;top:192px">Co-financed by government</div>
  <div class="page-badge"></div><span class="page-num">2</span><span class="page-brand">RTV</span>
</section>

<section class="slide s3" aria-label="Agenda">
  <h2 class="slide-title">The Time Is Now!</h2>
  <ul class="agenda">
    <li>Macro-environment &amp; Mortgage market: Green Light</li>
    <li>A sophisticated &amp; successful program: Catalyst</li>
    <li>Investment Structure of a typical project: Leverage &amp; Limited Risks</li>
    <li>Small &amp; mid size developers: A partner by choice</li>
    <li>RTV: Value added &amp; Risk mitigation</li>
    <li>RTP: RTV, part of an integrated family of companies</li>
    <li>Appendix: Next step…RTV Fund (2013)</li>
  </ul>
  <h3 class="section-title">Macro-environment &amp; Mortgage Market</h3>
  <div class="section-pill">Green Light<span class="num">1</span></div>
  <div class="page-badge"></div><span class="page-num">3</span><span class="page-brand">RTV</span>
</section>

<section class="slide s4" aria-label="Middle class">
  <h2 class="slide-title">A Middle Class Of 100 Million People…</h2>
  <p class="slide-sub" style="font-size:7.5px;width:280px;line-height:1.25">Strong political will &amp; positive income generation trends constitute grounds for a significant demand in social housing</p>
  <div class="card card-a">
    <div class="card-head">Politics</div>
    <p>Brazil launched a fierce battle against poverty 10 years ago with President Almar. The positive economic environment has helped implement these policies</p>
    <p><b>Growth Acceleration Program (2007-10): R$400B (*)</b><br>- Public investments in infrastructure<br>- Lightens the administrative and legal burden on private initiatives and long-term growth<br>- Stimulating Credit &amp; Financing for the real estate sector</p>
    <p><b>Growth Acceleration Program (2011-14): R$960B (*)</b><br>- Better City + &amp; Community: R$90B<br>- Water, Light, Transportation: R$130B<br>- Energy: R$460B<br>- <b>Housing: R$278B</b> – public financing and subsidies through various programs, notably <b>Casa Nova</b> for low and middle classes and <b>Credito Coletivo</b></p>
  </div>
  <div class="card card-b">
    <div class="card-head">Emergence Of The Middle Class</div>
    <p>- It reached remarkable success: poverty has decreased from 30% of population in 1990 to less than 20% in 2012</p>
    <p>- More than 40M people have recently entered the middle class. They need decent housing</p>
    <p><b>Middle class will represent 54% of the population</b> by the end of 2012 (overall population of 197M). Constitution of an upper middle class with an appetite for pricier products</p>
    <p><b>Housing deficit is estimated to be around 9M</b> of which 7M in urban housing</p>
  </div>
  <div class="page-badge"></div><span class="page-num">4</span><span class="page-brand">RTV</span>
</section>

<section class="slide s5" aria-label="Demographics">
  <h2 class="slide-title">…and Still Growing</h2>
  <p class="slide-sub" style="font-size:7.5px;width:280px;top:30px;line-height:1.25">Positive demographics &amp; economic environment will sustain the demanda</p>
  <svg class="charts" width="130" height="170" viewBox="0 0 130 170" role="img" aria-label="Charts of wage growth, unemployment, household income and population by class">
    <g fill="#3b7fc0">
      <rect x="10" y="18" width="5" height="24"/><rect x="18" y="14" width="5" height="28"/><rect x="26" y="20" width="5" height="22"/><rect x="34" y="16" width="5" height="26"/><rect x="42" y="12" width="5" height="30"/><rect x="50" y="18" width="5" height="24"/><rect x="58" y="22" width="5" height="20"/><rect x="66" y="17" width="5" height="25"/>
    </g>
    <polyline points="10,3 20,6 30,8 40,12 50,16 60,20 70,24" fill="none" stroke="#d6453a" stroke-width="1"/>
    <line x1="8" y1="42" x2="75" y2="42" stroke="#999" stroke-width=".5"/>
    <text x="40" y="6" font-size="3" fill="#333">Real Wage Growth</text>
    <g>
      <rect x="10" y="60" width="50" height="2.5" fill="#3b7fc0"/><rect x="10" y="63" width="40" height="2.5" fill="#d6453a"/>
      <rect x="10" y="68" width="56" height="2.5" fill="#3b7fc0"/><rect x="10" y="71" width="44" height="2.5" fill="#d6453a"/>
      <rect x="10" y="76" width="60" height="2.5" fill="#3b7fc0"/><rect x="10" y="79" width="48" height="2.5" fill="#d6453a"/>
      <rect x="10" y="84" width="52" height="2.5" fill="#3b7fc0"/><rect x="10" y="87" width="38" height="2.5" fill="#d6453a"/>
      <rect x="10" y="92" width="46" height="2.5" fill="#3b7fc0"/><rect x="10" y="95" width="30" height="2.5" fill="#d6453a"/>
    </g>
    <text x="20" y="118" font-size="3" fill="#333">Number of people per household income</text>
    <g>
      <rect x="14" y="140" width="8" height="20" fill="#3b7fc0"/><rect x="14" y="128" width="8" height="12" fill="#d6453a"/><rect x="14" y="122" width="8" height="6" fill="#7bb342"/><rect x="14" y="120" width="8" height="2" fill="#7d5aa8"/>
      <rect x="30" y="136" width="8" height="24" fill="#3b7fc0"/><rect x="30" y="126" width="8" height="10" fill="#d6453a"/><rect x="30" y="121" width="8" height="5" fill="#7bb342"/>
      <rect x="46" y="132" width="8" height="28" fill="#3b7fc0"/><rect x="46" y="124" width="8" height="8" fill="#d6453a"/><rect x="46" y="120" width="8" height="4" fill="#7bb342"/>
    </g>
    <g font-size="2.6" fill="#333"><text x="64" y="128">Class A</text><text x="64" y="136">Class B</text><text x="64" y="144">Class C</text><text x="64" y="152">Class D/E</text></g>
  </svg>
  <div class="card card-a">
    <div class="card-head">End-buyers</div>
    <p>- Aging population: <b>Average number of persons per household</b> shrunk from 3.7 in 1991 to 3.1 in 2010. Expected to remain around 3</p>
    <p>- Projection of 12M more people by 2020</p>
    <p><b>- Natural increase in number of households / housing demand</b></p>
    <p>- Considerable growth in real wages, average <b>5.5%</b> from 2003-2012</p>
    <p><b>-20M more people will have entered Class C from 2008 to 2014</b></p>
  </div>
  <div class="page-badge"></div><span class="page-num">5</span><span class="page-brand">RTV</span>
</section>

<section class="slide s6 cover" aria-label="Closing slide">
  <div class="cover-disc"></div>
  <div class="art art-family" role="img" aria-label="Photo of a smiling family"></div>
  <div class="brand"><span class="mark"></span>RTV</div>
  <div class="thanks">Thank You!</div>
  <div class="thanks-sub">for watching!</div>
</section>

</body>
</html>
```